Quillory Nest Business Card

I need a business card design. We are a collaborate online training company. Our colors are gray and green. Our website is QuilloryNest.com

I would like an area for a profile picture within the card

```html
<!DOCTYPE html>
<html lang="en">
<head>
<meta charset="utf-8">
<title>Quillory Nest Business Card</title>
<link rel="stylesheet" href="https://fonts.googleapis.com/css2?family=Source+Sans+3:wght@400;600;700&display=swap">
<style>
  :root {
    --page: #d9d9d9;
    --card-black: #000000;
    --card-paper: #efefef;
    --brand-green: #7ab829;
    --ink-dark: #2a2a2a;
    --ink-mid: #4a4a4a;
    --ink-light: #ffffff;
    --ink-soft: #d6d6d6;
    --photo-ring: #e6e6e6;
    --photo-fill-a: #c9cfc9;
    --photo-fill-b: #8e9498;
  }
  * { box-sizing: border-box; margin: 0; padding: 0; }
  html, body { width: 1200px; height: 960px; overflow: hidden; }
  body {
    background: var(--page);
    font-family: "Source Sans 3", sans-serif;
    position: relative;
  }
  .card {
    position: absolute;
    left: 240px;
    width: 720px;
    height: 411px;
    overflow: hidden;
    box-shadow: 0 6px 18px rgba(0,0,0,0.18);
  }
  .card-back { top: 50px; background: var(--card-black); }
  .card-front { top: 499px; display: flex; }

  /* back side */
  .back-brand {
    position: absolute;
    left: 0; right: 0; top: 0; bottom: 0;
    display: flex; align-items: center; justify-content: center; gap: 18px;
  }
  .back-brand .brand-dot {
    width: 44px; height: 44px; border-radius: 50%; background: var(--ink-light);
  }
  .back-brand .brand-name {
    color: var(--ink-light); font-size: 50px; font-weight: 600; letter-spacing: 0.5px;
  }

  /* front side */
  .front-info {
    width: 45%;
    background: var(--card-paper);
    position: relative;
    padding: 44px 40px;
  }
  .front-brand { display: flex; align-items: center; gap: 10px; }
  .front-brand .brand-dot {
    width: 26px; height: 26px; border-radius: 50%; background: var(--brand-green);
  }
  .front-brand .brand-name {
    color: var(--ink-dark); font-size: 28px; font-weight: 600;
  }
  .contact-list {
    position: absolute; left: 40px; bottom: 46px;
    list-style: none;
  }
  .contact-list li {
    display: flex; align-items: center; gap: 14px;
    color: var(--ink-mid); font-size: 17px; line-height: 27px;
  }
  .contact-list svg { width: 16px; height: 16px; flex: none; }

  .front-profile {
    width: 55%;
    background: var(--card-black);
    position: relative;
    display: flex; flex-direction: column; align-items: center;
  }
  .profile-photo {
    margin-top: 72px;
    width: 150px; height: 150px; border-radius: 50%;
    border: 6px solid var(--photo-ring);
    background: radial-gradient(circle at 50% 40%, var(--photo-fill-a), var(--photo-fill-b));
  }
  .profile-name {
    margin-top: 74px;
    color: var(--ink-light); font-size: 25px; font-weight: 700; line-height: 1;
  }
  .profile-title {
    margin-top: 6px;
    color: var(--ink-soft); font-size: 18px; font-weight: 400;
  }
</style>
</head>
<body>

<section class="card card-back">
  <div class="back-brand">
    <span class="brand-dot"></span>
    <span class="brand-name">Quillory Nest</span>
  </div>
</section>

<section class="card card-front">
  <div class="front-info">
    <div class="front-brand">
      <span class="brand-dot"></span>
      <span class="brand-name">Quillory Nest</span>
    </div>
    <ul class="contact-list">
      <li>
        <svg viewBox="0 0 16 16" aria-hidden="true"><path d="M4 1.5l2.2 3-1.4 1.6c.8 1.8 2.2 3.3 4.1 4.1l1.6-1.4 3 2.2-1.3 2.5C7 13.2 2.8 9 1.5 3.1z" fill="#8a8a8a"/></svg>
        <span>000-000-0000</span>
      </li>
      <li>
        <svg viewBox="0 0 16 16" aria-hidden="true"><rect x="1.5" y="3.5" width="13" height="9" fill="none" stroke="#8a8a8a" stroke-width="1.5"/><path d="M1.5 3.5L8 9l6.5-5.5" fill="none" stroke="#8a8a8a" stroke-width="1.5"/></svg>
        <span>abcd@quillorynest.com</span>
      </li>
      <li>
        <svg viewBox="0 0 16 16" aria-hidden="true"><circle cx="8" cy="8" r="6.5" fill="none" stroke="#8a8a8a" stroke-width="1.5"/><ellipse cx="8" cy="8" rx="2.8" ry="6.5" fill="none" stroke="#8a8a8a" stroke-width="1.2"/><path d="M1.5 8h13" stroke="#8a8a8a" stroke-width="1.2"/></svg>
        <span>www.quillorynest.com</span>
      </li>
    </ul>
  </div>
  <div class="front-profile">
    <div class="profile-photo" role="img" aria-label="Profile photo of the cardholder"></div>
    <p class="profile-name">Your Name</p>
    <p class="profile-title">Job Title</p>
  </div>
</section>

</body>
</html>
```